I am looking for help designing my new business cards. I would like rounded edges and a raised logo on the back of the card. I have 2 Logos. One with a boat in it and one without. I'd like the one on the back to be the one that includes the boat and just the name on the front. I have included multiple formats of my logo. Please let me know if you need anymore.

Target Market(s)

Potential buyers and other sales brokers

Industry/Entity Type

Sales - Yacht / Boat Sales

Contact Information for Business Card

Id liike the front to include just the business name portion of the logo along with my name (Corwin Dalby), phone number (555.318.6027), website address (www.dalbymarineco.example) and not my physical address but just "Port Verity, SC". The back should include my full logo that has the boat included. This portion I'd prefer raised amd take up the majority of the space there. Thanks!!

Colors
0054AA
0677BA
7BADD7
CADEEF
E8F1F8
0094D4
00A9DD
6FCCEA
C7EBF8
E9F6FB

Requirements
Must have
• Double sided
Nice to have
• My email address: Corwin@dalbymarineco.example The NMTG logo somewhere small on the front of the card
Should not have
• My full address, prefer only "Port Verity, SC"

```html
<!DOCTYPE html>
<html lang="en">
<head>
<meta charset="utf-8">
<title>Dalby Marine Co. — Business Card</title>
<link href="https://fonts.googleapis.com/css2?family=Poppins:wght@400;500;600;700&display=swap" rel="stylesheet">
<style>
  :root {
    --page: #000000;
    --navy: #20295f;
    --ink: #25306a;
    --blue: #0a84c2;
    --paper: #ffffff;
    --paper-shade: #f1f2f4;
    --white: #ffffff;
  }
  * { margin: 0; padding: 0; box-sizing: border-box; }
  html, body {
    width: 1009px; height: 1200px; overflow: hidden;
    background: var(--page);
    font-family: "Poppins", sans-serif;
  }
  .sheet { position: relative; width: 1009px; height: 1200px; }
  .card {
    position: absolute; left: 72px;
    width: 1125px; height: 675px;
    transform: scale(0.7689); transform-origin: top left;
    background: radial-gradient(ellipse at 50% 45%, var(--paper) 0%, var(--paper-shade) 100%);
    overflow: hidden;
  }
  .card--back { top: 64px; }
  .card--front { top: 618px; }

  .boat-art {
    position: absolute; left: 335px; top: 110px; width: 460px; height: 215px;
    background: linear-gradient(180deg, #e6ecf5 0%, #c9d9ee 60%, #8fc3e6 100%);
    border-radius: 6px;
  }
  .brand-name {
    position: absolute; left: 0; right: 0;
    text-align: center; color: var(--navy);
    font-weight: 700; letter-spacing: 1px; white-space: nowrap;
  }
  .card--back .brand-name { top: 355px; font-size: 52px; }
  .divider { position: absolute; left: 524px; top: 472px; width: 80px; height: 7px; background: var(--navy); }
  .card--back .site {
    position: absolute; left: 0; right: 0; top: 488px;
    text-align: center; font-size: 25px; color: var(--ink);
  }

  .shapes { position: absolute; inset: 0; width: 1125px; height: 675px; }
  .card--front .brand-name { left: 86px; right: auto; top: 108px; font-size: 41px; text-align: left; }
  .holder {
    position: absolute; left: 300px; top: 228px;
    font-size: 52px; font-weight: 500; color: var(--ink);
  }
  .contact { position: absolute; display: flex; align-items: center; color: var(--ink); }
  .contact--phone { left: 222px; top: 345px; font-size: 35px; font-weight: 500; gap: 20px; }
  .contact--mail { left: 460px; top: 460px; font-size: 26px; font-weight: 500; gap: 20px; }
  .rule { position: absolute; height: 7px; background: var(--navy); }
  .rule--phone { left: 160px; top: 424px; width: 408px; }
  .rule--mail { left: 583px; top: 520px; width: 408px; }
  .card--front .site {
    position: absolute; left: 383px; top: 563px;
    font-size: 24px; font-weight: 500; color: var(--ink);
  }
  .location {
    position: absolute; left: 775px; top: 78px; width: 300px;
    display: flex; flex-direction: column; align-items: center; gap: 14px;
    color: var(--white); font-size: 32px; white-space: nowrap;
  }
</style>
</head>
<body>
<div class="sheet">
  <section class="card card--back">
    <div class="boat-art" role="img" aria-label="Logo illustration of a center-console fishing boat on a blue wave"></div>
    <div class="brand-name">DALBY MARINE CO.</div>
    <div class="divider"></div>
    <div class="site">www.dalbymarineco.example</div>
  </section>

  <section class="card card--front">
    <svg class="shapes" viewBox="0 0 1125 675" aria-hidden="true">
      <polygon points="669,0 1125,0 1125,497 1053,497 669,82" fill="var(--blue)"/>
      <polygon points="701,119 1053,497 1125,497 1125,579 1086,579 701,165" fill="var(--navy)"/>
      <polygon points="0,302 346,675 0,675" fill="var(--navy)"/>
      <polygon points="0,383 33,383 303,675 0,675" fill="var(--blue)"/>
    </svg>
    <div class="brand-name">DALBY MARINE CO.</div>
    <div class="holder">Corwin Dalby</div>
    <div class="contact contact--phone">
      <svg width="36" height="50" viewBox="0 0 36 50" aria-hidden="true">
        <rect x="2" y="2" width="32" height="46" rx="5" fill="none" stroke="var(--ink)" stroke-width="3"/>
        <line x1="2" y1="9" x2="34" y2="9" stroke="var(--ink)" stroke-width="2"/>
        <line x1="2" y1="40" x2="34" y2="40" stroke="var(--ink)" stroke-width="2"/>
        <line x1="14" y1="5.5" x2="22" y2="5.5" stroke="var(--ink)" stroke-width="2"/>
      </svg>
      <span>555.318.6027</span>
    </div>
    <div class="rule rule--phone"></div>
    <div class="contact contact--mail">
      <svg width="50" height="34" viewBox="0 0 50 34" aria-hidden="true">
        <rect x="2" y="2" width="46" height="30" rx="3" fill="none" stroke="var(--ink)" stroke-width="3"/>
        <polyline points="3,4 25,20 47,4" fill="none" stroke="var(--ink)" stroke-width="3"/>
        <line x1="3" y1="31" x2="19" y2="16" stroke="var(--ink)" stroke-width="2.5"/>
        <line x1="47" y1="31" x2="31" y2="16" stroke="var(--ink)" stroke-width="2.5"/>
      </svg>
      <span>Corwin@dalbymarineco.example</span>
    </div>
    <div class="rule rule--mail"></div>
    <div class="site">www.dalbymarineco.example</div>
    <div class="location">
      <svg width="48" height="64" viewBox="0 0 48 64" aria-hidden="true">
        <path d="M24 61 C10 44 3 34 3 24 A21 21 0 0 1 45 24 C45 34 38 44 24 61 Z" fill="none" stroke="var(--white)" stroke-width="3.5"/>
        <circle cx="24" cy="23" r="8" fill="none" stroke="var(--white)" stroke-width="3"/>
      </svg>
      <span>Port Verity, SC</span>
    </div>
  </section>
</div>
</body>
</html>
```